We sell companies excess stock for them

We need a business card for a company based in New Zealand called 'StockHarbor'.

Check out our website to get an idea www.stockharbor.example

We help other businesses to;
- Sell Excess Stock
- Manage Product Returns
- Sell Company Assets

Our logo is attached for your reference
The font used is 'RifficFree-Bold'

Target Market(s)

Businesses

Industry/Entity Type

Business

Contact Information for Business Card

Name: Mark Pellow
Phone: 027 846 2093
email: markpellow@stockharbor.example
website: www.stockharbor.example

Font styles to use
Other font styles liked:
• Unsure

Colors
9bcb3b

Requirements
Must have
• coming soon
Nice to have
• coming soon
Should not have
• coming soon

```html
<!DOCTYPE html>
<html lang="en">
<head>
<meta charset="utf-8">
<title>StockHarbor Business Card</title>
<link rel="stylesheet" href="https://fonts.googleapis.com/css2?family=Fredoka+One&family=Montserrat:wght@400;500;600&display=swap">
<style>
  :root {
    --page-bg: #b4b4b4;
    --card-dark: #3a3c40;
    --card-dark-edge: #2b2d30;
    --brand-green: #8dbd22;
    --brand-green-light: #9bcb3b;
    --brand-green-deep: #78aa12;
    --ink: #141414;
    --white: #ffffff;
    --soft-white: #eef5dc;
  }
  * { box-sizing: border-box; margin: 0; padding: 0; }
  html, body { width: 1200px; height: 576px; overflow: hidden; }
  body {
    background: var(--page-bg);
    position: relative;
    font-family: "Montserrat", "Helvetica Neue", Arial, sans-serif;
  }
  .card {
    position: absolute;
    top: 138px;
    width: 484px;
    height: 294px;
    border-radius: 14px;
    overflow: hidden;
    box-shadow: 0 3px 8px rgba(0,0,0,0.35);
  }
  /* Front */
  .card-front {
    left: 82px;
    background: radial-gradient(ellipse at 70% 20%, #4a4c51 0%, var(--card-dark) 45%, var(--card-dark-edge) 100%);
  }
  .front-wordmark {
    position: absolute;
    left: 40px;
    top: 100px;
    font-family: "Fredoka One", "Arial Rounded MT Bold", "Arial Black", sans-serif;
    font-weight: 700;
    font-size: 52px;
    line-height: 50px;
    letter-spacing: -0.5px;
    color: var(--white);
  }
  .mascot-area {
    position: absolute;
    left: 238px;
    top: 26px;
    width: 240px;
    height: 262px;
    border-radius: 40px;
    background: radial-gradient(ellipse at 50% 45%, #8fbe3a 0%, #d9a54a 45%, rgba(60,62,66,0) 75%);
  }
  /* Back */
  .card-back {
    left: 602px;
    background: linear-gradient(160deg, var(--brand-green-light) 0%, var(--brand-green) 55%, var(--brand-green-deep) 100%);
  }
  .back-wordmark {
    position: absolute;
    right: 26px;
    top: 36px;
    font-family: "Fredoka One", "Arial Rounded MT Bold", "Arial Black", sans-serif;
    font-weight: 700;
    font-size: 32px;
    line-height: 36px;
    letter-spacing: -0.5px;
    color: var(--ink);
  }
  .mascot-watermark {
    position: absolute;
    left: 4px;
    top: 16px;
    width: 250px;
    height: 210px;
    border-radius: 60px;
    background: radial-gradient(ellipse at 45% 45%, rgba(255,255,255,0.18) 0%, rgba(255,255,255,0) 70%);
  }
  .edge-notch {
    position: absolute;
    left: -14px;
    top: 222px;
    width: 28px;
    height: 34px;
    border-radius: 50%;
    background: var(--card-dark);
  }
  .holder {
    position: absolute;
    left: 30px;
    top: 218px;
    display: flex;
    align-items: center;
  }
  .holder-name {
    font-weight: 600;
    font-size: 18px;
    color: var(--soft-white);
    padding-right: 6px;
    border-right: 1.5px solid var(--ink);
    line-height: 20px;
  }
  .holder-role {
    font-size: 9.5px;
    color: var(--ink);
    padding-left: 6px;
  }
  .contact-row {
    position: absolute;
    left: 28px;
    right: 14px;
    top: 250px;
    display: flex;
    align-items: center;
    gap: 6px;
    font-size: 9.6px;
    color: var(--ink);
    white-space: nowrap;
  }
  .contact-item { display: flex; align-items: center; gap: 3px; }
  .contact-item svg { width: 10px; height: 10px; fill: var(--soft-white); flex: none; }
</style>
</head>
<body>
  <section class="card card-front">
    <div class="front-wordmark">Stock<br>Harbor</div>
    <div class="mascot-area" role="img" aria-label="Cartoon delivery courier mascot giving a thumbs up and carrying a parcel"></div>
  </section>

  <section class="card card-back">
    <div class="mascot-watermark" role="img" aria-label="Faint tone-on-tone courier mascot decoration"></div>
    <div class="back-wordmark">StockHarbor</div>
    <div class="edge-notch"></div>
    <div class="holder">
      <span class="holder-name">Mark Pellow</span>
      <span class="holder-role">Managing Director</span>
    </div>
    <div class="contact-row">
      <span class="contact-item">
        <svg viewBox="0 0 16 16"><path d="M1 5c0-2 2-3 7-3s7 1 7 3v2h-4V5H5v2H1z M3 8h10l1 6H2z"/></svg>
        027 846 2093
      </span>
      <span class="contact-item">
        <svg viewBox="0 0 16 16"><path d="M1 3h14v10H1z M1 3l7 6 7-6" stroke="#8dbd22" stroke-width="1.2"/></svg>
        markpellow@stockharbor.example
      </span>
      <span class="contact-item">
        <svg viewBox="0 0 16 16"><circle cx="8" cy="8" r="7"/><path d="M1 8h14M8 1c-3 4-3 10 0 14M8 1c3 4 3 10 0 14" stroke="#8dbd22" fill="none" stroke-width="1"/></svg>
        www.stockharbor.example
      </span>
    </div>
  </section>
</body>
</html>
```